Prestige Car Bodyshop Business Card

We are a car bodyshop based in the UK. Our customer base is mainly prestige high-value vehicles. I am looking for a classy and stylish business card design for my staff to give out to customers, with their direct email and phone number, as well as our main email and phone number with address details

I am also looking to have a general business card design with just our main company address and contact details, but also have a space to add a manufacturer approval logo (i.e Falcora, Vexa, Torvik etc... logo) in the corner somewhere.

I do not particularly want any outlines or pictures of cars on the card, I would just like a quality high-end look.

Please feel free to get in touch if you have any questions or queries?

Many Thanks

Gordon

Target Market(s)

Prestige vehicle owners

Industry/Entity Type

Automotive

Contact Information for Business Card

I am looking for a classy and stylish business card design for my staff to give out to customers, with their direct email and phone number, as well as our main email and phone number with address details

Font styles to use
Sans Serif

Colors

Designer to choose colors to be used in the design.

Requirements
Nice to have
• I do not particularly want any outlines or pictures of cars on the card, I would just like a quality high-end look.

```html
<!DOCTYPE html>
<html lang="en">
<head>
<meta charset="utf-8">
<title>Harlow Accident Repair Centre – Business Cards</title>
<link rel="stylesheet" href="https://fonts.googleapis.com/css2?family=Arimo:wght@400;700&family=Josefin+Sans:wght@300;400&display=swap">
<style>
  :root {
    --page: #ffffff;
    --navy-deep: #173566;
    --navy-mid: #1a4f93;
    --blue-bright: #1467b8;
    --white: #ffffff;
    --rule: rgba(255,255,255,0.75);
    --accent: #f28a1e;
    --badge-a: #c9ced6;
    --badge-b: #b82a2a;
    --badge-c: #3f7d4a;
    --badge-d: #8a93a3;
  }
  * { margin: 0; padding: 0; box-sizing: border-box; }
  html, body { width: 1200px; height: 683px; overflow: hidden; background: var(--page); }
  .canvas { position: relative; width: 1200px; height: 683px; }
  .card {
    position: absolute; top: 252px; width: 295px; height: 180px; overflow: hidden;
    color: var(--white);
    background: linear-gradient(160deg, var(--navy-deep) 0%, var(--navy-mid) 55%, var(--blue-bright) 100%);
    font-family: "Arimo", Arial, sans-serif;
  }
  .card--general { left: 139px; }
  .card--staff { left: 459px; }
  .card--back { left: 766px; }
  .pos { position: absolute; }

  .brand-ring { position: absolute; border-radius: 50%; border: 1.2px solid var(--white);
    background: radial-gradient(circle at 40% 35%, #1d4a8a, #143062); }
  .brand-name { position: absolute; font-family: "Josefin Sans", sans-serif; font-weight: 300;
    color: var(--white); letter-spacing: 0.02em; white-space: nowrap; line-height: 1; }
  .brand-rule { position: absolute; height: 1px; background: var(--rule); }
  .brand-tag { position: absolute; font-family: "Josefin Sans", sans-serif; font-weight: 300;
    color: var(--white); letter-spacing: 0.06em; white-space: nowrap; line-height: 1; }

  .divider-rule { position: absolute; height: 1px; background: var(--rule); }
  .address { font-size: 7.6px; white-space: nowrap; }
  .contact-line { position: absolute; font-size: 7.6px; white-space: nowrap; display: flex; align-items: center; gap: 3px; line-height: 1; }
  .contact-line svg { width: 6px; height: 6px; fill: var(--white); }
  .column-split { position: absolute; width: 1px; background: var(--rule); }
  .staff-name { font-size: 11.5px; font-weight: 700; white-space: nowrap; }
  .staff-role { font-size: 7.8px; white-space: nowrap; }
  .approvals { position: absolute; display: flex; gap: 3px; align-items: center; }
  .web-address { position: absolute; left: 0; width: 100%; text-align: center; top: 161px;
    font-size: 10.5px; letter-spacing: 0.12em; }
</style>
</head>
<body>
<div class="canvas">

  <svg width="0" height="0" style="position:absolute">
    <symbol id="icon-phone" viewBox="0 0 10 10"><path d="M1 3.2C1 2 2.5 1 5 1s4 1 4 2.2L7.6 4 6.8 2.8H3.2L2.4 4zM2.6 4.5h4.8L8.6 9H1.4z"/></symbol>
    <symbol id="icon-fax" viewBox="0 0 10 10"><path d="M3 1h4v2H3zM1 3.5h8V9H1zM2.5 5h1v1h-1zM4.5 5h1v1h-1zM6.5 5h1v1h-1z"/></symbol>
    <symbol id="icon-mail" viewBox="0 0 10 10"><path d="M1 2h8v6H1zM1.8 2.8v.3L5 5.4l3.2-2.3v-.3zM1.8 4v3.2h6.4V4L5 6.3z" fill-rule="evenodd"/></symbol>
    <symbol id="icon-globe" viewBox="0 0 10 10"><path d="M5 .8a4.2 4.2 0 1 0 0 8.4A4.2 4.2 0 0 0 5 .8zm0 1c.5.5.9 1.4 1 2.6H4c.1-1.2.5-2.1 1-2.6zM1.9 5.4h1.3c.1 1.1.4 2 .8 2.6a3.2 3.2 0 0 1-2.1-2.6zm0-1A3.2 3.2 0 0 1 4 1.9c-.4.6-.7 1.5-.8 2.5zM5 8.2c-.5-.5-.9-1.4-1-2.8h2c-.1 1.4-.5 2.3-1 2.8zm1-.2c.4-.6.7-1.5.8-2.6h1.3A3.2 3.2 0 0 1 6 8zm.8-3.6c-.1-1-.4-1.9-.8-2.5a3.2 3.2 0 0 1 2.1 2.5z"/></symbol>
  </svg>

  <!-- General company card -->
  <section class="card card--general">
    <div class="brand-ring" style="left:22px;top:15px;width:42px;height:42px;"></div>
    <div class="brand-name" style="left:70px;top:27px;font-size:16px;">HARLOW</div>
    <div class="brand-rule" style="left:70px;top:44px;width:78px;"></div>
    <div class="brand-tag" style="left:70px;top:48px;font-size:5.6px;">ACCIDENT REPAIR CENTRE</div>

    <div class="divider-rule" style="left:22px;top:104px;width:252px;"></div>
    <div class="pos address" style="left:22px;top:113px;">Eastmoor Lane, Kingsford, Avonbridge, AB12 3CD</div>
    <div class="contact-line" style="left:22px;top:128px;"><svg><use href="#icon-phone"/></svg>0117 496 0123</div>
    <div class="contact-line" style="left:22px;top:139px;"><svg><use href="#icon-fax"/></svg>0117 496 0456</div>
    <div class="column-split" style="left:121px;top:126px;height:24px;"></div>
    <div class="contact-line" style="left:128px;top:128px;"><svg><use href="#icon-mail"/></svg>info@harlowrepairs.co.uk</div>
    <div class="contact-line" style="left:128px;top:139px;"><svg><use href="#icon-globe"/></svg>www.harlowrepairs.co.uk</div>

    <svg class="approvals" style="left:161px;top:163px;" width="126" height="10" role="img" aria-label="Manufacturer approval badges">
      <rect x="0" y="2" width="12" height="6" rx="3" fill="var(--badge-a)"/>
      <ellipse cx="21" cy="5" rx="7" ry="4" fill="var(--badge-c)"/>
      <rect x="31" y="3" width="14" height="4" rx="2" fill="var(--badge-d)"/>
      <rect x="48" y="2" width="13" height="6" rx="1" fill="var(--badge-b)"/>
      <rect x="64" y="6" width="8" height="1" fill="var(--badge-a)"/>
      <rect x="75" y="1" width="5" height="7" fill="var(--badge-a)"/>
      <rect x="83" y="4" width="16" height="2" fill="var(--badge-b)"/>
      <circle cx="106" cy="5" r="3.6" fill="var(--badge-d)"/>
      <circle cx="116" cy="5" r="3.6" fill="var(--badge-c)"/>
    </svg>
  </section>

  <!-- Staff card -->
  <section class="card card--staff">
    <div class="brand-ring" style="left:21px;top:15px;width:34px;height:34px;"></div>
    <div class="brand-name" style="left:59px;top:23px;font-size:13px;">HARLOW</div>
    <div class="brand-rule" style="left:59px;top:37px;width:62px;"></div>
    <div class="brand-tag" style="left:59px;top:40px;font-size:4.6px;">ACCIDENT REPAIR CENTRE</div>

    <div class="pos staff-name" style="left:21px;top:88px;">John Doe</div>
    <div class="pos staff-role" style="left:89px;top:91px;">Manager</div>
    <div class="divider-rule" style="left:20px;top:106px;width:251px;"></div>
    <div class="pos address" style="left:21px;top:114px;">Eastmoor Lane, Kingsford, Avonbridge, AB12 3CD</div>
    <div class="contact-line" style="left:21px;top:129px;"><svg><use href="#icon-phone"/></svg>0117 496 0123</div>
    <div class="contact-line" style="left:21px;top:140px;"><svg><use href="#icon-fax"/></svg>0117 496 0456</div>
    <div class="column-split" style="left:120px;top:127px;height:24px;"></div>
    <div class="contact-line" style="left:127px;top:129px;"><svg><use href="#icon-mail"/></svg>info@harlowrepairs.co.uk</div>
    <div class="contact-line" style="left:127px;top:140px;"><svg><use href="#icon-globe"/></svg>www.harlowrepairs.co.uk</div>

    <svg class="approvals" style="left:156px;top:161px;" width="126" height="10" role="img" aria-label="Manufacturer approval badges">
      <rect x="0" y="2" width="12" height="6" rx="3" fill="var(--badge-a)"/>
      <ellipse cx="21" cy="5" rx="7" ry="4" fill="var(--badge-c)"/>
      <rect x="31" y="3" width="14" height="4" rx="2" fill="var(--badge-d)"/>
      <rect x="48" y="2" width="13" height="6" rx="1" fill="var(--badge-b)"/>
      <rect x="64" y="6" width="8" height="1" fill="var(--badge-a)"/>
      <rect x="75" y="1" width="5" height="7" fill="var(--badge-a)"/>
      <rect x="83" y="4" width="16" height="2" fill="var(--badge-b)"/>
      <circle cx="106" cy="5" r="3.6" fill="var(--badge-d)"/>
      <circle cx="116" cy="5" r="3.6" fill="var(--badge-c)"/>
    </svg>
  </section>

  <!-- Card reverse -->
  <section class="card card--back">
    <div class="brand-ring" style="left:45px;top:45px;width:70px;height:70px;"></div>
    <div class="brand-name" style="left:124px;top:62px;font-size:25px;">HARLOW</div>
    <div class="brand-rule" style="left:124px;top:88px;width:124px;"></div>
    <div class="brand-tag" style="left:125px;top:94px;font-size:8.6px;">ACCIDENT REPAIR CENTRE</div>
    <div class="web-address">www.harlowrepairs.co.uk</div>
  </section>

</div>
</body>
</html>
```